Wordpress design for media production company

We are a small production company called Copper Lantern Pictures specializing in documentary and short film.

We are after a wordpress web site that is fun and engaging with a relaxed feel. We would like to be able to easily edit and maintain the website ourselves.

We would like:
* A title screen that has a photo taking up most of the screen.
* Contact details (inc. social media links) on a static bar at the bottom.
* An area for our previous work. Some thumbnails or icons that open up and embedded youtube or vimeo video.
* An area for "about us" which will have information on the company and links to separate profiles of 3 (initially) employees.
* A Blog.
* Somewhere to show what we are currently working on.
* Examples of other stuff we have done (ie. photography, poetry, audio, animation and VFX).

We already have a logo that can be animated. It would be very cool to have it as a "Loading" page while things load in the background.

The text needs to be fun but easy to read.

We already have a license for "Q Layout" which seems pretty cool and flexible, so if you wanted to use it then great but if not then that is fine too.

A couple of pages that we like are:
http://www.plumvistaworks.com/
http://dorianfelke.com/
http://www.tilestackhub.com/

Please do not hesitate to contact me if you would like more information on anything.

Cheers

Rupert

Target Market(s)

Mainly Australian clients seeking media services
Broadcasting companies

Industry/Entity Type

It Company

Requirements
Nice to have
• I love the parallax look on http://www.plumvistaworks.com/

```html
<!DOCTYPE html>
<html lang="en">
<head>
<meta charset="utf-8">
<title>Copper Lantern Pictures</title>
<link href="https://fonts.googleapis.com/css2?family=Comfortaa:wght@400;700&family=Montserrat:wght@600;700&family=Open+Sans:wght@400;600;700&display=swap" rel="stylesheet">
<style>
:root{
  --red:#b3140f;
  --red-bright:#d81b12;
  --black:#050505;
  --page:#111214;
  --panel:#1b1c1f;
  --card:#202124;
  --band:#2b2b2c;
  --line:#3a3a3c;
  --text:#cfcfcf;
  --muted:#5d5e61;
  --white:#ffffff;
}
*{box-sizing:border-box;margin:0;padding:0}
html,body{width:1200px;height:3371px;overflow:hidden;background:var(--page);font-family:"Open Sans",Arial,sans-serif;color:var(--text)}
.page{position:relative;width:1200px;height:3371px;overflow:hidden;background:var(--page)}
.abs{position:absolute}

/* header */
.site-header{left:0;top:0;width:1200px;height:146px;background:var(--black)}
.brand{left:101px;top:40px;display:flex;align-items:center;gap:14px}
.brand-mark{width:64px;height:64px;border-radius:50%;background:var(--white)}
.brand-name{font-family:"Montserrat",sans-serif;font-weight:700;font-size:27px;color:var(--white);line-height:1.1;width:230px}
.main-nav{top:66px;left:0;width:1200px;font-size:13px;color:#d8d8d8}
.main-nav span{position:absolute;white-space:nowrap}
.main-nav .current{font-weight:700;color:var(--white)}

.user-bar{left:0;top:146px;width:1200px;height:63px;background:var(--red);border-bottom:2px solid #5a0805}
.avatar{left:122px;top:156px;width:48px;height:48px;border-radius:50%;background:linear-gradient(#9c8a7e,#5e4b42);border:2px solid #d0d0d0}
.welcome{left:180px;top:160px;font-size:13px;line-height:20px;color:var(--white)}
.welcome b{color:#f5a300;font-weight:400}
.search{left:876px;top:162px;width:225px;height:36px;background:#8e0f0b;border:1px solid #6f0a07}

/* hero */
.hero{left:0;top:209px;width:1200px;height:634px;background:radial-gradient(ellipse at 50% 40%,#2c2a27 0%,#161514 55%,#0b0b0b 100%)}
.hero-title{left:0;top:236px;width:1200px;text-align:center;font-family:"Montserrat",sans-serif;font-weight:600;font-size:22px;letter-spacing:1px;color:var(--white)}
.slide{border:1px solid #000;box-shadow:0 0 20px #000}
.slide-main{left:452px;top:276px;width:301px;height:466px;background:linear-gradient(#9a9a96,#54524e 50%,#1f2224)}
.hero-arrow{font-size:56px;color:#e6e6e6;font-family:"Open Sans",sans-serif;top:532px}
.slide-bar{left:452px;top:742px;width:301px;height:49px;background:#1a1a1a;border-top:1px solid #333}
.mini-share{left:596px;top:800px;width:64px;height:20px;background:#2a2a2a;border-radius:3px}

.play{position:absolute;border-radius:50%;background:rgba(20,20,20,.8);border:3px solid rgba(90,90,90,.6)}

/* sections */
.section-title{font-family:"Comfortaa",sans-serif;font-size:20px;color:#d0d0d0;padding-left:16px;border-left:7px solid var(--red);height:42px;line-height:50px}
.section-rule{height:1px;background:var(--line)}

.work-card{background:var(--panel);border:1px solid #2a2b2e;width:238px;height:303px}
.work-card .thumb-head{position:absolute;left:8px;top:12px;width:30px;height:22px;background:linear-gradient(#d28a88,#8e4b4a)}
.work-card .menu{position:absolute;right:10px;top:14px;width:18px;height:14px;border-top:2px solid #999;border-bottom:2px solid #999}
.work-card .menu::after{content:"";position:absolute;left:0;top:4px;width:18px;height:2px;background:#999}
.work-card .media{position:absolute;left:0;top:54px;width:236px;height:198px}
.work-card .caption{position:absolute;left:10px;top:266px;font-size:13px;color:#bbb}
.work-card .share{position:absolute;left:146px;top:262px;width:54px;height:24px;background:#3a3a3c;border-radius:2px;font-size:12px;color:#ddd;text-align:center;line-height:24px}
.work-card .plus{position:absolute;left:210px;top:258px;font-size:22px;color:#999}

.filter{height:18px;background:#2a2b2e;border:1px solid #3c3c3e;font-size:10px;color:#aaa;line-height:16px;padding-left:6px}

.about-copy{left:97px;width:1006px;text-align:center;font-size:12.5px;line-height:22px;color:var(--muted)}
.experts-title{left:0;top:1650px;width:1200px;text-align:center;font-size:22px;color:var(--white);font-weight:600}
.experts-sub{left:0;top:1690px;width:1200px;text-align:center;font-size:12.5px;color:var(--muted)}
.expert-tab{height:25px;font-size:13px;text-align:center;line-height:25px;color:var(--white);background:var(--red-bright);border-radius:2px}
.expert-tab.active{background:#bdbdbd;color:var(--red)}

.current-band{left:0;top:1964px;width:1200px;height:443px;background:var(--band)}
.player-controls{left:326px;top:2321px;width:519px;height:54px;background:#151515}

.stuff-card{width:223px;height:239px;background:var(--card);text-align:center}
.stuff-card .icon{position:absolute;left:62px;top:26px;width:99px;height:99px;border-radius:50%;background:#0c0c0d}
.stuff-card .label{position:absolute;left:0;top:141px;width:100%;font-size:13.5px;color:#e0e0e0}
.stuff-card p{position:absolute;left:14px;top:169px;width:195px;font-size:11.5px;line-height:17px;color:var(--muted)}

.tweet-band{left:0;top:2883px;width:1200px;height:121px;background:#1b1e21}
.tweet-bubble{left:531px;top:2836px;width:84px;height:84px;border-radius:50%;background:#2a2d31}
.tweet-quote{left:0;top:2926px;width:1200px;text-align:center;font-size:20px;color:#c8c8c8}
.tweet-quote em{font-style:normal;color:var(--red-bright)}

.footer{left:0;top:3004px;width:1200px;height:265px;background:var(--page)}
.footer-title{font-size:11px;font-weight:700;color:var(--white)}
.post-text{font-size:10px;line-height:17px;color:var(--muted);width:150px}
.more{font-size:9px;color:var(--white);background:var(--red-bright);border-radius:3px;padding:1px 5px}
.photo{width:86px;height:83px;border:2px solid #ddd}
.tag{height:22px;font-size:10px;line-height:22px;color:#aaa;background:#2a2b2e;padding:0 8px}
.tag.hot{background:var(--red-bright);color:var(--white)}

.bottom-bar{left:0;top:3269px;width:1200px;height:102px;background:#0c0d0e;border-top:1px solid #222}
.foot-links{left:101px;top:3306px;font-size:11px;font-weight:700;color:var(--white);letter-spacing:.5px}
.foot-links b{color:var(--red-bright)}
.social{width:34px;height:34px;border-radius:50%;background:#3a3b3e;top:3297px}
.social.hot{background:var(--red-bright)}
</style>
</head>
<body>
<div class="page">

  <header class="abs site-header"></header>
  <div class="abs brand">
    <div class="brand-mark"></div>
    <div class="brand-name">Copper Lantern Pictures</div>
  </div>
  <nav class="abs main-nav">
    <span style="left:501px">Home</span>
    <span class="current" style="left:584px">About Us</span>
    <span style="left:687px">Services</span>
    <span style="left:783px">News &amp; Tips</span>
    <span style="left:905px">Portfolio</span>
    <span style="left:1006px">Quote Request</span>
  </nav>

  <div class="abs user-bar"></div>
  <div class="abs avatar" role="img" aria-label="Visitor avatar photo"></div>
  <div class="abs welcome"><b>Welcome !</b> Guest<br>info@copperlantern-pictures.net</div>
  <div class="abs search">
    <svg width="20" height="20" viewBox="0 0 20 20" style="position:absolute;left:10px;top:8px"><circle cx="11" cy="8" r="4.5" fill="none" stroke="#fff" stroke-width="2"/><line x1="8" y1="11" x2="3" y2="16" stroke="#fff" stroke-width="2.5"/></svg>
  </div>

  <!-- hero slider -->
  <section class="abs hero" role="img" aria-label="Dark misty forest backdrop"></section>
  <h1 class="abs hero-title">SPECIALIZING IN DOCUMENTARY AND SHORT FILM</h1>
  <div class="abs hero-arrow" style="left:44px">«</div>
  <div class="abs hero-arrow" style="left:1116px">»</div>
  <div class="abs slide" style="left:128px;top:420px;width:171px;height:306px;background:linear-gradient(135deg,#3a3c35,#121310)" role="img" aria-label="Film still of a helmeted figure"></div>
  <div class="abs slide" style="left:303px;top:420px;width:146px;height:306px;background:linear-gradient(#5a3a2c,#2a1a14)" role="img" aria-label="Film still of a creature close-up"></div>
  <div class="abs slide" style="left:755px;top:420px;width:144px;height:306px;background:linear-gradient(#1d1d22,#38302a)" role="img" aria-label="Film still of a night street"></div>
  <div class="abs slide" style="left:903px;top:420px;width:171px;height:306px;background:linear-gradient(135deg,#1a1a1a,#2c2a12)" role="img" aria-label="Film still of a costumed hero"></div>
  <div class="abs slide slide-main" role="img" aria-label="Featured film still of a rocky tower in mist"></div>
  <div class="play" style="left:544px;top:451px;width:116px;height:116px"></div>
  <svg class="abs" style="left:580px;top:484px" width="50" height="50" viewBox="0 0 50 50"><polygon points="6,2 46,25 6,48" fill="var(--red-bright)"/></svg>
  <div class="abs slide-bar">
    <svg style="position:absolute;left:18px;top:6px" width="22" height="18" viewBox="0 0 22 18"><rect x="2" y="2" width="16" height="10" rx="2" fill="none" stroke="#aaa" stroke-width="1.5"/><polygon points="5,12 10,12 5,16" fill="#aaa"/></svg>
    <svg style="position:absolute;left:90px;top:4px" width="22" height="20" viewBox="0 0 22 20"><path d="M11 18 L3 10 A4.5 4.5 0 0 1 11 4 A4.5 4.5 0 0 1 19 10 Z" fill="var(--red-bright)"/></svg>
    <svg style="position:absolute;left:162px;top:4px" width="20" height="20" viewBox="0 0 20 20"><circle cx="15" cy="4" r="2.5" fill="#ddd"/><circle cx="5" cy="10" r="2.5" fill="#ddd"/><circle cx="15" cy="16" r="2.5" fill="#ddd"/><path d="M15 4 L5 10 L15 16" stroke="#ddd" fill="none"/></svg>
    <div style="position:absolute;left:210px;top:8px;width:80px;height:22px;background:#101010;color:var(--red-bright);font-size:12px;text-align:center;letter-spacing:2px;line-height:22px">★★★★</div>
    <div style="position:absolute;left:8px;top:32px;width:285px;font-size:8px;color:#666;display:flex;justify-content:space-around"><span>Comment</span><span>Like it</span><span>Share it</span><span></span></div>
  </div>
  <div class="abs mini-share"></div>

  <!-- previous works -->
  <div class="abs section-title" style="left:101px;top:868px">Previous Works</div>
  <div class="abs section-rule" style="left:262px;top:900px;width:780px"></div>
  <div class="abs" style="left:1040px;top:890px;width:26px;height:22px;background:#2a2b2e;color:#999;font-size:10px;text-align:center;line-height:22px">◄</div>
  <div class="abs" style="left:1074px;top:890px;width:26px;height:22px;background:#2a2b2e;color:#999;font-size:10px;text-align:center;line-height:22px">►</div>
  <div class="abs filter" style="left:906px;top:928px;width:89px">Fantasy</div>
  <div class="abs filter" style="left:1002px;top:928px;width:43px">All</div>
  <svg class="abs" style="left:1060px;top:930px" width="42" height="14" viewBox="0 0 42 14"><g fill="#bbb"><rect x="0" y="0" width="6" height="6"/><rect x="8" y="0" width="6" height="6"/><rect x="0" y="8" width="6" height="6"/><rect x="8" y="8" width="6" height="6"/><rect x="26" y="0" width="4" height="4"/><rect x="32" y="0" width="4" height="4"/><rect x="38" y="0" width="4" height="4"/><rect x="26" y="5" width="4" height="4"/><rect x="32" y="5" width="4" height="4"/><rect x="38" y="5" width="4" height="4"/><rect x="26" y="10" width="4" height="4"/><rect x="32" y="10" width="4" height="4"/><rect x="38" y="10" width="4" height="4"/></g></svg>

  <div class="abs work-card" style="left:99px;top:973px">
    <div class="thumb-head"></div><div class="menu"></div>
    <div class="media" style="background:linear-gradient(90deg,#3c3026,#7a6a58 60%,#2e2a26)" role="img" aria-label="Period drama film still"></div>
    <div class="play" style="left:93px;top:128px;width:52px;height:52px"></div>
    <svg style="position:absolute;left:112px;top:144px" width="20" height="20" viewBox="0 0 20 20"><polygon points="2,1 19,10 2,19" fill="var(--red-bright)"/></svg>
    <div class="caption">Lorem Ipsum De</div><div class="share">Share</div><div class="plus">+</div>
  </div>
  <div class="abs work-card" style="left:353px;top:973px">
    <div class="thumb-head"></div><div class="menu"></div>
    <div class="media" style="background:linear-gradient(90deg,#d8d8d8,#6a6a6a 55%,#222)" role="img" aria-label="Black and white music video still"></div>
    <div style="position:absolute;left:0;top:232px;width:236px;height:20px;background:#0c0c0c"><div style="position:absolute;left:28px;top:8px;width:70px;height:4px;background:#3a8dd8"></div></div>
    <div class="caption">Lorem Ipsum De</div><div class="share">Share</div><div class="plus">+</div>
  </div>
  <div class="abs work-card" style="left:607px;top:973px">
    <div class="thumb-head"></div><div class="menu"></div>
    <div class="media" style="background:linear-gradient(135deg,#c0b0a0,#6a5040 55%,#2a1a14)" role="img" aria-label="Guitarist performance still"></div>
    <div class="play" style="left:93px;top:128px;width:52px;height:52px"></div>
    <svg style="position:absolute;left:112px;top:144px" width="20" height="20" viewBox="0 0 20 20"><polygon points="2,1 19,10 2,19" fill="var(--red-bright)"/></svg>
    <div class="caption">Lorem Ipsum De</div><div class="share">Share</div><div class="plus">+</div>
  </div>
  <div class="abs work-card" style="left:863px;top:973px">
    <div class="thumb-head"></div><div class="menu"></div>
    <div class="media" style="background:linear-gradient(90deg,#3c3026,#7a6a58 60%,#2e2a26)" role="img" aria-label="Period drama film still"></div>
    <div class="play" style="left:93px;top:128px;width:52px;height:52px"></div>
    <svg style="position:absolute;left:112px;top:144px" width="20" height="20" viewBox="0 0 20 20"><polygon points="2,1 19,10 2,19" fill="var(--red-bright)"/></svg>
    <div class="caption">Lorem Ipsum De</div><div class="share">Share</div><div class="plus">+</div>
  </div>

  <!-- about us -->
  <div class="abs section-title" style="left:101px;top:1342px">About Us</div>
  <div class="abs section-rule" style="left:218px;top:1376px;width:883px"></div>
  <p class="abs about-copy" style="top:1414px">Simply dummy text of the printing and typesetting industry. Lorem Ipsum has been the industry's standard dummy text ever since the 1500s, when an unknown printer took a galley of type and scrambled it to make a type specimen book. It has survived not only five centuries, but also the leap into electronic typesetting, remaining essentially unchanged. It was popularised in the 1960s with the release of Inkpress sheets containing Lorem Ipsum passages, and more recently with desktop publishing software like Vellum Pagesetter including versions of Lorem Ipsum.</p>
  <p class="abs about-copy" style="top:1524px">simply dummy text of the printing and typesetting industry. Lorem Ipsum has been the industry's standard dummy text ever since the 1500s, when an unknown printer took a galley of type and scrambled it to make a type specimen book. It has survived not only five centuries, but also the leap into electronic typesetting, remaining essentially unchanged. It was popularised in the 1960s with the release of Inkpress sheets containing Lorem Ipsum passages, and more recently with desktop publishing software like Vellum Pagesetter including versions of Lorem Ipsum.</p>
  <h2 class="abs experts-title">Our Outstanding Experts</h2>
  <p class="abs experts-sub">(Lorem Ipsum has been the industry's standard dummy text ever since the 1500s)</p>
  <div class="abs expert-tab active" style="left:377px;top:1723px;width:151px">Mira Tolland</div>
  <div class="abs expert-tab" style="left:539px;top:1723px;width:135px">Owen Brisk</div>
  <div class="abs expert-tab" style="left:683px;top:1723px;width:148px">Owen Brisk</div>
  <div class="abs" style="left:377px;top:1775px;width:146px;height:142px;background:linear-gradient(#6a5a50,#2a2420);border:2px solid #222" role="img" aria-label="Team member portrait"></div>

  <!-- currently working on -->
  <section class="abs current-band"></section>
  <div class="abs section-title" style="left:101px;top:1984px">We are currently Working On</div>
  <div class="abs section-rule" style="left:412px;top:2016px;width:756px"></div>
  <div class="abs" style="left:326px;top:2047px;width:519px;height:274px;background:radial-gradient(ellipse at 50% 30%,#7a7a7a,#2a2a2a 55%,#0c0c0c)" role="img" aria-label="DJ performing to a crowd"></div>
  <div class="play" style="left:542px;top:2182px;width:62px;height:62px"></div>
  <svg class="abs" style="left:564px;top:2201px" width="24" height="24" viewBox="0 0 24 24"><polygon points="2,1 23,12 2,23" fill="var(--red-bright)"/></svg>
  <div class="abs player-controls">
    <svg style="position:absolute;left:14px;top:10px" width="200" height="20" viewBox="0 0 200 20"><rect x="2" y="3" width="14" height="9" rx="2" fill="none" stroke="#aaa" stroke-width="1.5"/><path d="M72 17 L65 10 A4 4 0 0 1 72 5 A4 4 0 0 1 79 10 Z" fill="var(--red-bright)"/><circle cx="138" cy="4" r="2" fill="#ddd"/><circle cx="130" cy="10" r="2" fill="#ddd"/><circle cx="138" cy="16" r="2" fill="#ddd"/><polygon points="184,6 178,10 184,14" fill="#ddd"/><polygon points="190,6 184,10 190,14" fill="#ddd"/></svg>
    <svg style="position:absolute;left:218px;top:14px" width="40" height="16" viewBox="0 0 40 16"><polygon points="4,1 16,8 4,15" fill="#fff"/><polygon points="26,3 32,8 26,13" fill="#ddd"/><polygon points="31,3 37,8 31,13" fill="#ddd"/></svg>
    <div style="position:absolute;left:272px;top:8px;font-size:8px;color:#888">Movie name · 12:00 · full movie</div>
    <div style="position:absolute;left:272px;top:24px;width:160px;height:3px;background:#444"><div style="width:64px;height:3px;background:var(--red-bright)"></div></div>
    <svg style="position:absolute;left:470px;top:14px" width="40" height="16" viewBox="0 0 40 16"><polygon points="1,5 5,5 10,1 10,15 5,11 1,11" fill="#ddd"/><path d="M28 2 H24 V6 M34 2 H38 V6 M28 14 H24 V10 M34 14 H38 V10" stroke="#ddd" fill="none" stroke-width="1.5"/></svg>
  </div>

  <!-- stuff we have done -->
  <div class="abs section-title" style="left:101px;top:2440px">Stuff We Have Done</div>
  <div class="abs section-rule" style="left:333px;top:2472px;width:768px"></div>
  <div class="abs stuff-card" style="left:103px;top:2541px"><div class="icon" role="img" aria-label="Photographer character illustration" style="background:radial-gradient(circle,#c07a3a 0 30%,#0c0c0d 31%)"></div><div class="label">PHOTOGRAPHY</div><p>Simply dummy text of the printing and typesetting industry. Lorem Ipsum has been the industry's standard dummy</p></div>
  <div class="abs stuff-card" style="left:360px;top:2541px"><div class="icon" role="img" aria-label="Poet character illustration" style="background:radial-gradient(circle,#c8b8a8 0 30%,#0c0c0d 31%)"></div><div class="label">POETRY</div><p>Simply dummy text of the printing and typesetting industry. Lorem Ipsum has been the industry's standard dummy</p></div>
  <div class="abs stuff-card" style="left:613px;top:2541px"><div class="icon" role="img" aria-label="Audio character illustration" style="background:radial-gradient(circle,#3a6ab8 0 22%,#0c0c0d 23%)"></div><div class="label">AUDIO</div><p>Simply dummy text of the printing and typesetting industry. Lorem Ipsum has been the industry's standard dummy</p></div>
  <div class="abs stuff-card" style="left:870px;top:2541px"><div class="icon" role="img" aria-label="Animation characters illustration" style="background:radial-gradient(circle,#5aa878 0 28%,#0c0c0d 29%)"></div><div class="label">ANIMATION</div><p>Simply dummy text of the printing and typesetting industry. Lorem Ipsum has been the industry's standard dummy</p></div>

  <!-- quote band -->
  <section class="abs tweet-band"></section>
  <div class="abs tweet-bubble"></div>
  <div class="abs" style="left:1010px;top:2868px;font-size:10px;color:#777;letter-spacing:6px">◄►</div>
  <p class="abs tweet-quote">Praesent ac <em>condimentum</em> felis. Nulla at <em>nisl orci</em>, at dignissim dolor</p>

  <!-- footer -->
  <section class="abs footer"></section>
  <div class="abs footer-title" style="left:101px;top:3030px">RECENT POSTS</div>
  <div class="abs" style="left:101px;top:3067px;width:63px;height:61px;background:linear-gradient(#e0e0e0,#7a7a7a);border:2px solid #ddd" role="img" aria-label="Post thumbnail photo"></div>
  <p class="abs post-text" style="left:183px;top:3070px">Pellentesque ut nunc neque,eu pharetra pretium scelerisque massaPellentes.</p>
  <span class="abs more" style="left:342px;top:3123px">Read More</span>
  <div class="abs" style="left:101px;top:3184px;width:63px;height:63px;background:linear-gradient(#e0e0e0,#7a7a7a);border:2px solid #ddd" role="img" aria-label="Post thumbnail photo"></div>
  <p class="abs post-text" style="left:183px;top:3186px">Pellentesque ut nunc neque,eu pharetra pretium scelerisque massaPellentes.</p>
  <span class="abs more" style="left:342px;top:3240px">Read More</span>

  <div class="abs footer-title" style="left:488px;top:3024px">PHOTO STREAM</div>
  <div class="abs photo" style="left:488px;top:3060px;background:linear-gradient(#b8c8d8,#5a6a7a)" role="img" aria-label="Stream photo of a woman in sunglasses"></div>
  <div class="abs photo" style="left:598px;top:3060px;background:linear-gradient(#e8e0d0,#a09080)" role="img" aria-label="Stream photo of a portrait"></div>
  <div class="abs photo" style="left:703px;top:3060px;background:linear-gradient(90deg,#e8e8e8,#3a3a3a)" role="img" aria-label="Stream photo of a split portrait"></div>
  <div class="abs photo" style="left:488px;top:3162px;background:linear-gradient(#b8c8d8,#5a6a7a)" role="img" aria-label="Stream photo of a woman in sunglasses"></div>
  <div class="abs photo" style="left:598px;top:3162px;background:linear-gradient(#e8e0d0,#a09080)" role="img" aria-label="Stream photo of a portrait"></div>
  <div class="abs photo" style="left:703px;top:3162px;background:linear-gradient(90deg,#e8e8e8,#3a3a3a)" role="img" aria-label="Stream photo of a split portrait"></div>

  <div class="abs footer-title" style="left:883px;top:3054px">FEED WIDGET</div>
  <div class="abs" style="left:883px;top:3092px;width:184px;height:22px;background:#2a2b2e"></div>
  <div class="abs" style="left:1074px;top:3092px;width:27px;height:22px;background:#2a2b2e;color:#ccc;text-align:center;line-height:22px">+</div>
  <div class="abs" style="left:883px;top:3124px;font-size:9px;color:#777">DON'T WORRY, WE DON'T SPAM EVER</div>
  <span class="abs tag" style="left:883px;top:3162px">portfolio</span>
  <span class="abs tag hot" style="left:945px;top:3162px">site theme</span>
  <span class="abs tag" style="left:1040px;top:3162px">layouts</span>
  <span class="abs tag" style="left:883px;top:3193px">Premium template</span>
  <span class="abs tag" style="left:988px;top:3193px">responsive</span>
  <span class="abs tag" style="left:1055px;top:3193px">clean</span>
  <span class="abs tag" style="left:883px;top:3222px">psd web theme</span>

  <section class="abs bottom-bar"></section>
  <div class="abs foot-links"><b>HOME</b> / PAGES / MEDIA / BLOG / CONTACT</div>
  <div class="abs social" style="left:843px"></div>
  <div class="abs social hot" style="left:884px"></div>
  <div class="abs social" style="left:924px"></div>
  <div class="abs social" style="left:965px"></div>
  <div class="abs social" style="left:1005px"></div>

</div>
</body>
</html>
```